Korvanta Business Card

Looking for business card ideas. Company name is Korvanta. Have a few basic ideas on attachment. Please submit anything with the logo and general information from attachment.

Industry/Entity Type

Business

```html
<!DOCTYPE html>
<html lang="en">
<head>
<meta charset="utf-8">
<title>Korvanta Business Card</title>
<link href="https://fonts.googleapis.com/css2?family=Lato:wght@400;700&display=swap" rel="stylesheet">
<style>
  :root {
    --stage: #6b6b6b;
    --card-white: #ffffff;
    --brand-red: #ec2127;
    --brand-yellow: #fcd20a;
    --text-white: #ffffff;
  }
  * { margin: 0; padding: 0; box-sizing: border-box; }
  html, body {
    width: 1200px; height: 899px; overflow: hidden;
    background: var(--stage);
    font-family: "Lato", Arial, sans-serif;
  }
  .card {
    position: absolute; left: 150px; top: 192px;
    width: 900px; height: 514px;
    background: var(--card-white);
    border-radius: 26px; overflow: hidden;
  }
  .card-shapes { position: absolute; inset: 0; }
  .brand {
    position: absolute; left: 0; right: 0; top: 82px;
    display: flex; justify-content: center; align-items: center; gap: 22px;
  }
  .brand-dot {
    width: 92px; height: 92px; border-radius: 50%;
    background: var(--brand-red);
  }
  .brand-name {
    font-size: 68px; font-weight: 700; color: var(--brand-red);
    letter-spacing: 2px;
  }
  .holder {
    position: absolute; left: 0; right: 0; top: 268px;
    text-align: center; color: var(--text-white);
    font-size: 40px; font-weight: 400;
  }
  .holder strong { font-weight: 700; }
  .holder .title { color: var(--brand-yellow); font-size: 26px; font-weight: 700; }
  .contact-list {
    position: absolute; left: 32px; top: 356px;
    list-style: none; color: var(--text-white); font-size: 28px;
  }
  .contact-list li { display: flex; align-items: center; gap: 10px; height: 46px; }
  .contact-list .label { margin-left: 12px; }
  .location-list {
    position: absolute; right: 30px; top: 326px;
    list-style: none; color: var(--text-white); font-size: 24px; text-align: right;
  }
  .location-list li { display: flex; justify-content: flex-end; align-items: center; gap: 10px; height: 40px; }
  .icon {
    width: 26px; height: 26px; flex: none;
    background: var(--brand-yellow); border-radius: 3px;
  }
  .icon-gap { width: 26px; flex: none; }
</style>
</head>
<body>
  <div class="card">
    <svg class="card-shapes" viewBox="0 0 900 514" width="900" height="514">
      <path d="M0 360 Q470 150 900 330 L900 514 L0 514 Z" fill="var(--brand-red)"/>
      <path d="M0 352 Q470 138 900 320 L900 330 Q470 150 0 360 Z" fill="var(--brand-yellow)"/>
    </svg>

    <div class="brand">
      <span class="brand-dot"></span>
      <span class="brand-name">Korvanta</span>
    </div>

    <p class="holder">Dorian <strong>Vesk</strong><span class="title">, Dir.</span></p>

    <ul class="contact-list">
      <li>
        <svg class="icon" viewBox="0 0 26 26"><rect width="26" height="26" rx="3" fill="var(--brand-yellow)"/><rect x="5" y="8" width="16" height="11" fill="none" stroke="var(--brand-red)" stroke-width="2"/><path d="M5 8 L13 15 L21 8" fill="none" stroke="var(--brand-red)" stroke-width="2"/></svg>
        <span>(555) 014-2270</span><span class="label">Office</span>
      </li>
      <li>
        <svg class="icon" viewBox="0 0 26 26"><rect width="26" height="26" rx="3" fill="var(--brand-yellow)"/><rect x="8" y="4" width="10" height="18" rx="2" fill="var(--brand-red)"/><rect x="10" y="7" width="6" height="10" fill="var(--brand-yellow)"/></svg>
        <span>(555) 019-3346</span><span class="label">Cell</span>
      </li>
      <li>
        <svg class="icon" viewBox="0 0 26 26"><rect width="26" height="26" rx="3" fill="var(--brand-yellow)"/><path d="M5 11 Q13 5 21 11 L19 13 L16 11 L10 11 L7 13 Z" fill="var(--brand-red)"/><rect x="7" y="14" width="12" height="7" rx="1" fill="var(--brand-red)"/></svg>
        <span>dvesk@korvanta.com</span>
      </li>
    </ul>

    <ul class="location-list">
      <li>
        <span>2480 N. Harlow Ave.</span>
        <svg class="icon" viewBox="0 0 26 26"><rect width="26" height="26" rx="3" fill="var(--brand-yellow)"/><path d="M13 22 L7 12 A6 6 0 1 1 19 12 Z" fill="var(--brand-red)"/><circle cx="13" cy="10" r="2.4" fill="var(--brand-yellow)"/></svg>
      </li>
      <li><span>Brenton, TX 70412</span><span class="icon-gap"></span></li>
      <li>
        <span>www.korvanta.org</span>
        <svg class="icon" viewBox="0 0 26 26"><rect width="26" height="26" rx="3" fill="var(--brand-yellow)"/><g fill="none" stroke="var(--brand-red)" stroke-width="2.4"><rect x="5" y="11" width="10" height="6" rx="3" transform="rotate(-45 10 14)"/><rect x="11" y="9" width="10" height="6" rx="3" transform="rotate(-45 16 12)"/></g></svg>
      </li>
    </ul>
  </div>
</body>
</html>
```